Harrowfen Logistics, Project

Company Profile
Harrowfen Logistics Sdn Bhd is a well established and experienced freight forwarder in Kuala Lumpur, Malaysia. We specialize in air and sea forwarding, Custom Brokerage and regulatory compliance services, inland transportation,
overseas freighting and warehousing and distribution management. With our dedicated qualified and experienced professionals, we are fully committed to serving our clients.

Our Mission
Based on the motto “Quick, Reliable and Polite”, Harrowfen Logistics is dedicated to upholding the following three points corporate philosophy:
1. Adhering to the principle that “the customer always comes first”.
2. Contributing to the development of the local community.
3. Making it our duty to be responsible and sincere.

Our Edge
• One-Stop Logistics Solutions
• Extensive Network Throughout Malaysia
• Highly Qualified and Experienced Pool of Professionals
• Comprehensive IT Solutions
• Innovative and Customer-focused Solutions
• Flexible and Consistent in Managing Exceptions
• Total Supply Chain Visibility

Target Market(s)

We sell the logistics services to all the industry in Malaysia. (ONE Stop Logistics Solutions)

Industry/Entity Type

Logistic

Contact Information for Business Card

I want the back of the card to be white with the logo and slogan. i would like to see the logo on the front with the general info.

Requirements
Must have
• Name, Title, Office, Cell, Fax, Email, Address, Website
Nice to have
• Modern Design Business Card

```html
<!DOCTYPE html>
<html lang="en">
<head>
<meta charset="utf-8">
<title>Harrowfen Logistics – Stationery</title>
<link rel="stylesheet" href="https://fonts.googleapis.com/css2?family=Questrial&display=swap">
<style>
  :root {
    --bg: #d2d2d4;
    --paper: #f4f4f4;
    --blue-deep: #4a72b5;
    --blue-light: #66a6d9;
    --blue-line: #4f86c8;
    --grey-swoosh: #6e6e6e;
    --ink: #3a3a3a;
    --ink-soft: #5a5a5a;
  }
  * { margin: 0; padding: 0; box-sizing: border-box; }
  html, body { width: 1200px; height: 991px; overflow: hidden; }
  body {
    background: var(--bg);
    font-family: "Questrial", "Century Gothic", sans-serif;
    color: var(--ink);
    position: relative;
  }
  .sheet { position: absolute; background: var(--paper); overflow: hidden; }
  .swoosh { position: absolute; left: 0; bottom: 0; width: 100%; }
  .wordmark { position: absolute; white-space: nowrap; color: var(--ink); line-height: 1.15; }
  .wordmark span { display: block; }
  .wordmark--light { color: #fff; }

  .letterhead { left: 71px; top: 104px; width: 398px; height: 561px; }
  .letterhead .wordmark { left: 32px; top: 76px; font-size: 13px; }
  .contact { position: absolute; font-size: 5.6px; line-height: 1.3; color: var(--ink-soft); }
  .contact li { list-style: none; display: flex; align-items: center; gap: 3px; white-space: nowrap; }
  .contact .dot { width: 5px; height: 5px; background: var(--blue-line); border-radius: 1px; display: inline-block; flex: none; }
  .contact .addr { margin-top: 3px; }
  .letterhead .contact { left: 295px; top: 41px; }

  .folder {
    left: 507px; top: 90px; width: 433px; height: 575px;
    background: linear-gradient(180deg, var(--blue-deep), var(--blue-light));
    border-radius: 3px;
  }
  .folder .spine { position: absolute; left: 27px; top: 0; bottom: 0; width: 1px; background: rgba(255,255,255,0.18); }
  .folder .wordmark { left: 0; right: 0; top: 128px; text-align: center; font-size: 18px; }

  .card-front { left: 66px; top: 696px; width: 171px; height: 96px; }
  .card-front .wordmark { left: 10px; top: 36px; font-size: 8px; }
  .card-front .divider { position: absolute; left: 84px; top: 16px; width: 1px; height: 54px; background: #c8c8c8; }
  .card-front .person { position: absolute; left: 97px; top: 14px; }
  .person .name { font-size: 5.4px; color: var(--blue-deep); font-weight: 700; letter-spacing: .2px; }
  .person .title { font-size: 4px; color: var(--ink-soft); }
  .card-front .contact { left: 97px; top: 29px; font-size: 3.8px; }
  .card-front .contact .dot { width: 3.5px; height: 3.5px; }
  .card-front .contact .addr { margin-top: 2px; }

  .card-back { left: 66px; top: 810px; width: 171px; height: 95px; }
  .card-back .wordmark { left: 0; right: 0; top: 36px; text-align: center; font-size: 9px; }
  .card-back .slogan { position: absolute; left: 0; right: 0; top: 52px; text-align: center; font-size: 4.6px; color: var(--blue-deep); letter-spacing: .3px; }

  .comp-slip { left: 266px; top: 696px; width: 416px; height: 209px; }
  .comp-slip .wordmark { left: 23px; top: 64px; font-size: 12.5px; }
  .comp-slip .address { position: absolute; left: 28px; top: 172px; font-size: 5px; line-height: 1.3; color: var(--ink-soft); }

  .envelope { left: 718px; top: 696px; width: 416px; height: 209px; }
  .envelope .flap { position: absolute; left: 0; top: 0; width: 100%; height: 60px; }
  .envelope .wordmark { left: 0; right: 0; top: 24px; text-align: center; font-size: 8px; }
  .envelope .web { position: absolute; left: 0; right: 0; top: 181px; text-align: center; font-size: 5px; color: var(--ink-soft); }
</style>
</head>
<body>

  <section class="sheet letterhead">
    <div class="wordmark"><span>Harrowfen Logistics</span></div>
    <ul class="contact">
      <li><i class="dot"></i>01632 960418</li>
      <li><i class="dot"></i>info@harrowfen.com</li>
      <li><i class="dot"></i>www.harrowfen.com</li>
      <li class="addr">B12 Wren Park, Wren Park,</li>
      <li>Ashcombe, GX9 2QD</li>
    </ul>
    <svg class="swoosh" viewBox="0 0 398 30" height="30" preserveAspectRatio="none">
      <path d="M0 30 L0 14 C90 26 170 0 290 2 C340 3 375 12 398 22 L398 30 Z" fill="var(--blue-line)"/>
      <path d="M120 30 C190 10 270 4 320 6 C355 8 380 16 398 26 L398 30 Z" fill="#e6e6e6"/>
      <path d="M150 30 C210 14 280 8 320 10 C350 12 370 18 385 30 Z" fill="var(--grey-swoosh)"/>
    </svg>
  </section>

  <section class="sheet folder">
    <div class="spine"></div>
    <div class="wordmark wordmark--light"><span>Harrowfen Logistics</span></div>
  </section>

  <section class="sheet card-front">
    <div class="wordmark"><span>Harrowfen Logistics</span></div>
    <div class="divider"></div>
    <div class="person">
      <div class="name">MAYA TENNANT</div>
      <div class="title">General Manager</div>
    </div>
    <ul class="contact">
      <li><i class="dot"></i>Office: 01632 960418</li>
      <li><i class="dot"></i>Cell: 07700 900274</li>
      <li><i class="dot"></i>Fax: 01632 960419</li>
      <li><i class="dot"></i>info@harrowfen.com</li>
      <li><i class="dot"></i>www.harrowfen.com</li>
      <li class="addr">B12 Wren Park, Wren Park</li>
      <li>Ashcombe, GX9 2QD</li>
    </ul>
    <svg class="swoosh" viewBox="0 0 171 10" height="10" preserveAspectRatio="none">
      <path d="M0 10 L0 5 C40 9 70 0 120 1 C145 2 160 5 171 8 L171 10 Z" fill="var(--blue-line)"/>
      <path d="M55 10 C85 4 115 2 135 3 C150 4 162 7 168 10 Z" fill="var(--grey-swoosh)"/>
    </svg>
  </section>

  <section class="sheet card-back">
    <div class="wordmark"><span>Harrowfen Logistics</span></div>
    <p class="slogan">Quick, Reliable and Polite</p>
  </section>

  <section class="sheet comp-slip">
    <div class="wordmark"><span>Harrowfen Logistics</span></div>
    <p class="address">B12 Wren Park, Wren Park<br>Ashcombe, GX9 2QD</p>
    <svg class="swoosh" viewBox="0 0 416 28" height="28" preserveAspectRatio="none">
      <path d="M0 28 L0 12 C100 24 180 0 300 2 C350 3 390 12 416 22 L416 28 Z" fill="var(--blue-line)"/>
      <path d="M130 28 C200 10 280 4 330 6 C365 8 395 16 416 26 L416 28 Z" fill="#e6e6e6"/>
      <path d="M160 28 C220 12 290 8 330 10 C360 12 385 18 400 28 Z" fill="var(--grey-swoosh)"/>
    </svg>
  </section>

  <section class="sheet envelope">
    <svg class="flap" viewBox="0 0 416 60" preserveAspectRatio="none">
      <defs>
        <linearGradient id="flap-fill" x1="0" y1="0" x2="0" y2="1">
          <stop offset="0" stop-color="var(--blue-deep)"/>
          <stop offset="1" stop-color="#507dbf"/>
        </linearGradient>
      </defs>
      <path d="M0 0 H416 L400 54 Q398 58 392 58 H26 Q18 58 16 54 Z" fill="url(#flap-fill)"/>
    </svg>
    <div class="wordmark wordmark--light"><span>Harrowfen Logistics</span></div>
    <p class="web">www.harrowfen.com</p>
  </section>

</body>
</html>
```